Electrical contracting business specialising in smoke detector installation needs flyer design

i need a flyer design made up highlighting the fact that the Qld legislation is changing on smoke detectors in homes for everyones safety. I am an electrical contractor ( Tandrell Electrical) specialising in smoke detector installation to comply with the new Qld legislation. Some of the wording that can be used-
When you sleep, your sense of smell also sleeps. If a fire starts, toxic fumes canovercome you. Photoelectric smoke alarms see smoke and will alert you early, so you can escape. With interconnected alarms, you will be alerted no matter where you are, or where the fire starts.
New legislation specifies the type, positioning and interconnectedness of alarms, which are critical factors for an early warning and a quick escape.
To give your family the best chance of surviving a house fire, update your smoke alarms to match the new legislation as soon as you can. Call ME on 0418362957

Target Market(s)

Body Corporates , people selling and renting their properties

Industry/Entity Type

Electrician

Colors

Designer to choose colors to be used in the design.

Requirements
Must have
• Safety aspect.

```html
<!DOCTYPE html>
<html lang="en">
<head>
<meta charset="utf-8">
<title>Tandrell Electrical – Smoke Alarm Flyer</title>
<link rel="stylesheet" href="https://fonts.googleapis.com/css2?family=Cormorant+Garamond:wght@400;500&family=Source+Sans+3:wght@300;400;500&display=swap">
<style>
  :root {
    --charcoal: #3e3c3c;
    --gold: #b48a48;
    --gold-light: #c29a5a;
    --white: #ffffff;
    --cream: #f3ece0;
    --night: #08111f;
    --deep-blue: #1d3e63;
    --glow: #8fd0f5;
    --floor: #7d97ae;
  }
  * { margin: 0; padding: 0; box-sizing: border-box; }
  html, body { width: 857px; height: 1200px; overflow: hidden; background: #ffffff; }
  .flyer {
    position: relative;
    width: 857px;
    height: 1200px;
    overflow: hidden;
    font-family: "Source Sans 3", "Helvetica Neue", Arial, sans-serif;
    color: var(--white);
  }
  .masthead {
    position: absolute;
    left: 0; top: 0;
    width: 857px; height: 321px;
    background: var(--charcoal);
    text-align: center;
  }
  .brand-name {
    position: absolute;
    left: 0; right: 0; top: 120px;
    font-family: "Cormorant Garamond", Georgia, serif;
    font-weight: 400;
    font-size: 64px;
    line-height: 1;
    letter-spacing: 1px;
    color: var(--gold-light);
  }
  .brand-tagline {
    position: absolute;
    left: 0; right: 0; top: 226px;
    font-size: 17px;
    font-weight: 400;
    line-height: 27px;
    color: var(--gold-light);
  }
  .message {
    position: absolute;
    left: 0; top: 321px;
    width: 857px; height: 286px;
    background: var(--gold);
    padding: 46px 92px 0 102px;
  }
  .message p {
    font-size: 14.6px;
    font-weight: 500;
    line-height: 20px;
    margin-bottom: 20px;
  }
  .hero-visual {
    position: absolute;
    left: 0; top: 607px;
    width: 857px; height: 480px;
    background:
      radial-gradient(ellipse 90px 150px at 95px 150px, rgba(143,208,245,0.55), transparent 100%),
      radial-gradient(ellipse 90px 150px at 380px 150px, rgba(143,208,245,0.5), transparent 100%),
      radial-gradient(ellipse 80px 130px at 515px 120px, rgba(143,208,245,0.5), transparent 100%),
      radial-gradient(ellipse 80px 140px at 740px 150px, rgba(143,208,245,0.5), transparent 100%),
      radial-gradient(ellipse 120px 170px at 545px 320px, rgba(143,208,245,0.45), transparent 100%),
      radial-gradient(ellipse 600px 120px at 50% 60px, rgba(90,160,220,0.35), transparent 100%),
      linear-gradient(180deg, var(--night) 0%, var(--deep-blue) 22%, #3d6690 50%, var(--floor) 100%);
  }
  .contact-bar {
    position: absolute;
    left: 0; top: 1087px;
    width: 857px; height: 113px;
    background: var(--gold);
  }
  .contact-label {
    position: absolute;
    left: 100px; top: 42px;
    font-size: 18px;
    font-weight: 300;
    color: var(--cream);
  }
  .contact-phone {
    position: absolute;
    left: 104px; top: 65px;
    font-size: 19px;
    font-weight: 400;
    letter-spacing: 0.5px;
    color: var(--cream);
  }
  .contact-divider {
    position: absolute;
    left: 626px; top: 26px;
    width: 1px; height: 87px;
    background: var(--cream);
  }
  .footer-brand {
    position: absolute;
    left: 648px; top: 38px;
    color: var(--cream);
  }
  .footer-brand-name {
    font-family: "Cormorant Garamond", Georgia, serif;
    font-size: 24px;
    line-height: 1;
  }
  .footer-brand-sub {
    font-size: 9.5px;
    line-height: 13px;
    margin-top: 8px;
  }
</style>
</head>
<body>
<div class="flyer">
  <header class="masthead">
    <div class="brand-name">Tandrell Electrical</div>
    <div class="brand-tagline">Dane Tandrell<br>Electrical Contractor</div>
  </header>

  <section class="message">
    <p>When you sleep, your sense of smell also sleeps. If a fire starts, toxic fumes can over come you. Photoelectric smoke alarms see smoke and will alert you early, so you can escape. With interconnected alarms, you will be alerted no matter where you are, or where the fire starts.</p>
    <p>New legislation specifies the type, positioning and interconnectedness of alarms, which are critical factors for an early warning and a quick escape.</p>
    <p>To give your family the best chance of surviving a house fire, update your smoke alarms to match the new legislation as soon as you can.</p>
  </section>

  <div class="hero-visual" role="img" aria-label="Photo of a night-time home floor plan where glowing blue cones from interconnected ceiling smoke alarms cover every room, one person running to escape and another waking in bed"></div>

  <footer class="contact-bar">
    <div class="contact-label">For more Information Call</div>
    <div class="contact-phone">0418- 362- 957</div>
    <div class="contact-divider"></div>
    <div class="footer-brand">
      <div class="footer-brand-name">Tandrell Electrical</div>
      <div class="footer-brand-sub">Dane Tandrell<br>Electrical Contractor</div>
    </div>
  </footer>
</div>
</body>
</html>
```